i need a packaging design for italy sea food noodles, the size is 220mm*155mm*40mm. The aimed market is north America and European. Please use simple colours, not colorful. Here are the picture of my product, and one sample I found from supermarket. Please use the picture I uploaded, putting it on the cover of the packaging.

```html
<!DOCTYPE html>
<html lang="en">
<head>
<meta charset="UTF-8">
<title>Italy Sea Food Noodles – Front and Side Panels</title>
<link rel="stylesheet" href="https://fonts.googleapis.com/css2?family=Graduate&family=Playfair+Display:wght@500&family=Roboto:wght@900&display=swap">
<style>
  :root {
    --page-bg: #ececec;
    --basil: #1f6e38;
    --basil-deep: #155027;
    --mist: #e4ebe4;
    --wine: #8f1a21;
    --wine-deep: #5a0a0e;
    --side-light: #731417;
    --side-dark: #4f0a0c;
    --ribbon: #7d1418;
    --gold: #e8c21a;
    --white: #ffffff;
    --bowl: #1c1c1c;
    --pasta: #e8d6a2;
  }
  * { margin: 0; padding: 0; box-sizing: border-box; }
  html, body {
    width: 1161px; height: 1200px; overflow: hidden;
    background: var(--page-bg);
  }
  .carton {
    position: absolute; left: 215px; top: 150px;
    width: 731px; height: 900px;
    display: flex;
  }
  .front-panel {
    position: relative;
    width: 538px; height: 900px; overflow: hidden;
    background: linear-gradient(180deg,
      var(--basil-deep) 0%, var(--basil) 30%, #2f7a45 36%,
      #a9c4ae 40%, var(--mist) 43%, var(--mist) 48%,
      #d7cccb 58%, #b04a4f 70%, var(--wine) 78%, var(--wine-deep) 100%);
  }
  .side-panel {
    width: 193px; height: 900px;
    background: linear-gradient(180deg, var(--side-light) 0%, #6a1014 50%, var(--side-dark) 100%);
  }
  .dish-photo {
    position: absolute; left: 6px; top: 353px;
    width: 580px; height: 402px;
    border-radius: 50%;
    background:
      radial-gradient(ellipse at 48% 48%, var(--pasta) 0%, #dcc387 48%, #b89a5c 68%, var(--bowl) 72%, var(--bowl) 100%);
    box-shadow: 0 20px 32px rgba(40, 0, 0, 0.5);
  }
  .frame {
    position: absolute; left: 23px; top: 35px; right: 23px; bottom: 35px;
    border: 6px solid var(--white);
  }
  .origin-ribbon {
    position: absolute; left: 185px; top: 0;
    width: 170px; height: 158px;
    background: var(--ribbon);
    clip-path: polygon(0 0, 100% 0, 100% 100%, 50% 92%, 0 100%);
    text-align: center;
    padding-top: 70px;
    font-family: "Playfair Display", serif; font-weight: 500;
    font-size: 47px; line-height: 1; color: var(--white);
  }
  .rule {
    position: absolute; left: 82px; width: 359px; height: 3px;
    background: var(--gold);
  }
  .rule--top { top: 167px; }
  .rule--bottom { top: 254px; }
  .product-title {
    position: absolute; left: 0; width: 100%; top: 176px;
    text-align: center;
    font-family: "Graduate", serif; font-weight: 400; font-size: 72px; line-height: 1;
    color: var(--basil); -webkit-text-stroke: 1.5px var(--white);
    letter-spacing: 2px;
    transform: scaleY(1.22); transform-origin: top center;
  }
  .product-type {
    position: absolute; left: 0; width: 100%; top: 264px;
    text-align: center;
    font-family: "Roboto", sans-serif; font-weight: 900;
    font-size: 34px; line-height: 1; color: var(--white);
    letter-spacing: 1px;
  }
  .product-type .stars { font-size: 13px; vertical-align: middle; letter-spacing: 2px; }
</style>
</head>
<body>
  <div class="carton">
    <main class="front-panel">
      <div class="dish-photo" role="img" aria-label="Photo of seafood linguine with mussels, clams, shrimp, scallops and vegetables in a black bowl"></div>
      <div class="frame"></div>
      <div class="origin-ribbon">ITALY</div>
      <div class="rule rule--top"></div>
      <h1 class="product-title">SEA FOOD</h1>
      <div class="rule rule--bottom"></div>
      <p class="product-type"><span class="stars">★★</span> NOODLES <span class="stars">★★</span></p>
    </main>
    <aside class="side-panel"></aside>
  </div>
</body>
</html>
```